Bright Path Attorneys Billboard Design for Personal Injury Law Firm

Need a billboard design that we can use for different versions. 1400px X 400px jpeg or png
I have attached the logo and the attorney for the billboard. Attorney Marla Benning
Here is a link to our current website brightpathlegalgroup.example

HEADLINE: HIT BY A TRUCK?
SUBHEAD: NO FEE. BIG FIGHT.
877-GRANTLY

HEADLINE: ACCIDENT?
SUBHEAD: NO FEE, UNLESS WE WIN!
877-GRANTLY

HEADLINE: BIG TRUCK. BIG CASE.
SUBHEAD: YOU PAY $0 UPFRONT
877-GRANTLY

Target Market(s)

People in Car Accident

Industry/Entity Type

Personal Injury Attorneys

```html
<!DOCTYPE html>
<html lang="en">
<head>
<meta charset="utf-8">
<title>Bright Path Attorneys – Billboard</title>
<link rel="stylesheet" href="https://fonts.googleapis.com/css2?family=Oswald:wght@700&family=Roboto:wght@700;900&display=swap">
<style>
  :root {
    --page-bg: #e9ebee;
    --panel-bg: #f2f2ef;
    --brand-green: #5faa3c;
    --ink-dark: #2b2b2b;
    --white: #ffffff;
    --photo-steel: #5d6a72;
    --photo-shadow: #23282c;
    --photo-warm: #e59a45;
  }
  * { box-sizing: border-box; margin: 0; padding: 0; }
  html, body {
    width: 1200px;
    height: 1020px;
    overflow: hidden;
    background: var(--page-bg);
  }
  .billboard {
    position: absolute;
    left: 40px;
    top: 333px;
    width: 1120px;
    height: 354px;
    background: var(--panel-bg);
    overflow: hidden;
    box-shadow: 0 6px 24px rgba(0,0,0,0.12);
  }
  .crash-photo {
    position: absolute;
    left: 0; top: 0;
    width: 415px;
    height: 100%;
    background:
      radial-gradient(circle at 8% 6%, var(--photo-warm) 0%, rgba(229,154,69,0) 28%),
      linear-gradient(160deg, #8c959b 0%, var(--photo-steel) 40%, var(--photo-shadow) 100%);
  }
  .headline {
    position: absolute;
    right: 62px;
    top: 34px;
    font-family: "Oswald", sans-serif;
    font-weight: 700;
    font-size: 74px;
    line-height: 1;
    letter-spacing: 2px;
    color: var(--brand-green);
    white-space: nowrap;
  }
  .subhead {
    position: absolute;
    right: 60px;
    top: 114px;
    font-family: "Oswald", sans-serif;
    font-weight: 700;
    font-size: 58px;
    line-height: 1;
    letter-spacing: 1.5px;
    color: var(--ink-dark);
    white-space: nowrap;
  }
  .phone {
    position: absolute;
    right: 62px;
    top: 226px;
    display: flex;
    align-items: center;
    gap: 16px;
    font-family: "Roboto", sans-serif;
    font-weight: 900;
    font-size: 34px;
    color: var(--ink-dark);
  }
  .phone-icon { width: 34px; height: 34px; }
  .web-band {
    position: absolute;
    right: 0;
    top: 283px;
    height: 44px;
    padding: 0 62px 0 30px;
    background: var(--brand-green);
    border-radius: 22px 0 0 22px;
    font-family: "Roboto", sans-serif;
    font-weight: 700;
    font-size: 21px;
    line-height: 44px;
    color: var(--white);
    white-space: nowrap;
  }
  .firm-name {
    position: absolute;
    left: 440px;
    top: 289px;
    display: flex;
    align-items: center;
    gap: 10px;
    font-family: "Roboto", sans-serif;
    font-weight: 700;
    font-size: 20px;
    color: var(--ink-dark);
    white-space: nowrap;
  }
  .firm-square {
    width: 26px;
    height: 26px;
    background: var(--brand-green);
  }
</style>
</head>
<body>
  <section class="billboard">
    <div class="crash-photo" role="img" aria-label="Photo of the crumpled front end of a silver car after a collision, warm sunlight at upper left"></div>

    <h1 class="headline">HIT BY A TRUCK?</h1>
    <h2 class="subhead">NO FEE. BIG FIGHT.</h2>

    <div class="phone">
      <svg class="phone-icon" viewBox="0 0 34 34" aria-hidden="true">
        <circle cx="17" cy="17" r="15" fill="none" stroke="#5faa3c" stroke-width="2.5"/>
        <path d="M12.5 9.5c1-.6 1.8-.2 2.3.7l1.3 2.4c.4.8.2 1.5-.5 2l-1 .8c.8 1.8 2.1 3.2 3.9 4.1l.8-1c.5-.7 1.2-.9 2-.5l2.4 1.3c.9.5 1.2 1.4.6 2.3-1 1.6-2.6 2.4-4.5 1.8-4.1-1.4-7.3-4.6-8.6-8.7-.6-1.9.1-3.6 1.3-5.2z" fill="#5faa3c"/>
      </svg>
      <span class="phone-number">877-GRANTLY</span>
    </div>

    <div class="web-band">brightpathlegalgroup.example</div>

    <div class="firm-name">
      <span class="firm-square" aria-hidden="true"></span>
      <span>Bright Path Attorneys</span>
    </div>
  </section>
</body>
</html>
```